Dalvorn-Ke Photography needs a poster for a upcoming event

We need a Music Concert Poster designed for a musician named Marc T. Lindow. The concert is happening 6:30 pm, Saturday, January 10, 2015 Look to our current design ideas for inspiration. Keep it clean and simple but I want to see your creative ideas. Please view the throw togethers screenshots I have included in this project and then use one of the clean images in your design. Visit www.pinboardia.example/marclind/concert-posters/ for the musicians favorite music posters and gather ideas from there as well.

Industry/Entity Type

Event

Requirements
Nice to have
• Lets tend to lean towards a more sanserif font

```html
<!DOCTYPE html>
<html lang="en">
<head>
<meta charset="UTF-8">
<title>Marc T. Lindow in Concert</title>
<link rel="stylesheet" href="https://fonts.googleapis.com/css2?family=Raleway:wght@800&family=Oswald:wght@500&family=Josefin+Sans:ital,wght@1,400&family=Open+Sans:ital,wght@0,700;1,600&display=swap">
<style>
  :root {
    --bg-dark: #2f2d2c;
    --bg-mid: #7d7b79;
    --bg-light: #c4c2c0;
    --panel: rgba(58, 54, 52, 0.84);
    --text-light: #dcd8d6;
    --text-soft: #ece9e7;
    --accent: #5c4477;
    --shirt: #5b2f7c;
    --skin: #a57d66;
  }
  * { margin: 0; padding: 0; box-sizing: border-box; }
  html, body { width: 1200px; height: 600px; overflow: hidden; background: var(--bg-dark); }
  .poster { position: relative; width: 1200px; height: 600px; overflow: hidden; }

  .scene-photo {
    position: absolute; inset: 0;
    background:
      radial-gradient(ellipse 360px 420px at 1050px 560px, rgba(91,47,124,0.85), rgba(91,47,124,0.35) 55%, transparent 80%),
      radial-gradient(ellipse 200px 230px at 900px 230px, rgba(165,125,102,0.45), transparent 75%),
      radial-gradient(ellipse 520px 260px at 520px 110px, rgba(225,223,221,0.55), transparent 70%),
      radial-gradient(ellipse 600px 170px at 600px 580px, rgba(205,203,201,0.55), transparent 70%),
      linear-gradient(90deg, #4a4846 0%, var(--bg-mid) 30%, var(--bg-light) 52%, #8a8886 70%, #4b4948 86%, var(--bg-dark) 100%);
  }

  .info-panel {
    position: absolute; left: 20px; top: 213px; width: 693px; height: 283px;
    background: var(--panel);
  }
  .headliner {
    position: absolute; left: 26px; top: 12px;
    font-family: "Raleway", sans-serif; font-weight: 800;
    font-size: 86px; line-height: 1; letter-spacing: -3px;
    color: var(--text-light); white-space: nowrap;
  }
  .tagline {
    position: absolute; right: 16px; top: 96px;
    font-family: "Josefin Sans", sans-serif; font-style: italic;
    font-size: 46px; line-height: 1; color: var(--text-soft);
    text-transform: uppercase; white-space: nowrap;
  }
  .venue {
    position: absolute; left: 26px; top: 128px;
    font-family: "Open Sans", sans-serif; font-style: italic; font-weight: 600;
    font-size: 16px; line-height: 20px; letter-spacing: 0.6px; color: var(--text-soft);
    text-transform: uppercase; white-space: nowrap;
  }
  .showtime {
    position: absolute; right: 24px; top: 146px;
    font-family: "Open Sans", sans-serif; font-weight: 700;
    font-size: 15px; color: var(--text-soft); white-space: nowrap;
  }
  .event-date {
    position: absolute; left: 24px; top: 164px;
    font-family: "Oswald", sans-serif; font-weight: 500;
    font-size: 104px; line-height: 1; letter-spacing: 2px;
    color: var(--text-light);
    transform: scaleX(0.84); transform-origin: left top; white-space: nowrap;
  }
  .admission {
    position: absolute; left: 443px; top: 195px; width: 210px; height: 48px;
    background: var(--accent);
    display: flex; align-items: center; justify-content: center;
    font-family: "Open Sans", sans-serif; font-weight: 700;
    font-size: 16px; letter-spacing: 0.5px; color: #ffffff;
  }
</style>
</head>
<body>
  <main class="poster">
    <div class="scene-photo" role="img" aria-label="Soft-focus black and white photograph of a tree-lined country road, with the musician in a purple shirt holding an acoustic guitar on the right"></div>

    <section class="info-panel">
      <h1 class="headliner">MARC T. LINDOW</h1>
      <p class="tagline">in Concert</p>
      <p class="venue">Harbor Crest Community Church<br>427 Pelican Shore Rd Coral Haven, FL, 32500</p>
      <p class="showtime">AT 6:30 PM</p>
      <p class="event-date">01.10.2015</p>
      <p class="admission">FREE ENTRANCE!</p>
    </section>
  </main>
</body>
</html>
```